Business Card Design Project

I need a business card designed that is clean, simple and elegant.
I am a fashion and advertising photographer based in Cape Town and Durban South Africa.
check out my website: www.marlowvance.co.za for ideas
Updates
Hi all,
Thanks for your submissions so far!
Please note:
I want no more than than black, white and/or grey to be used.
I don't want any photos used.
I would like the card to be double sided.
I would like to continue the design similar to the past ones Ive used.
I hope this helps, please send me further questions should you have any.
many thanks!
Marlow
Hi,
Please have a look at the jpg I loaded(called inspiration) which is the direction or inspiration I am aiming at.
Also PLEASE remember NO PHOTOS to be included on the card
many thanks!!
Target Market(s)
You can look at my site to get a better understanding of the audience:
www.marlowvance.co.za
Industry/Entity Type
Advertising
Requirements
Must have
- Clean design which can also be used for a watermark on photographs
perhaps black background with white text/grey
company called: Marlow Vance Photography
Nice to have
- below I have added logos that I have used in the past.
Should not have
- pictures of cameras
tacky elements

```html
<!DOCTYPE html>
<html lang="en">
<head>
<meta charset="utf-8">
<title>Marlow Vance Photography – Business Card</title>
<link rel="stylesheet" href="https://fonts.googleapis.com/css2?family=Jura:wght@500;600;700&display=swap">
<style>
  :root {
    --card-bg: #000000;
    --ink-white: #ffffff;
    --ink-grey: #8e8e8e;
    --ornament-tone: #2a2a2a;
  }
  html, body {
    margin: 0;
    padding: 0;
    width: 1200px;
    height: 667px;
    overflow: hidden;
    background: var(--card-bg);
  }
  .business-card {
    position: relative;
    width: 1200px;
    height: 667px;
    background: var(--card-bg);
  }
  .business-card svg {
    display: block;
  }
  .ornament-area {
    position: absolute;
    left: 0;
    top: 0;
    width: 550px;
    height: 400px;
    background: radial-gradient(ellipse at 30% 25%, var(--ornament-tone) 0%, var(--card-bg) 75%);
  }
  .brand-text {
    position: absolute;
    left: 0;
    top: 0;
  }
  .brand-name {
    font-family: "Jura", sans-serif;
    font-weight: 600;
    font-size: 60px;
    fill: var(--ink-white);
  }
  .brand-tagline {
    font-family: "Jura", sans-serif;
    font-weight: 700;
    font-size: 42px;
    fill: var(--ink-grey);
  }
</style>
</head>
<body>
  <main class="business-card">
    <div class="ornament-area" role="img" aria-label="Decorative white dotted swirl lines curving in from the top-left corner"></div>
    <svg class="brand-text" width="1200" height="667" viewBox="0 0 1200 667" aria-label="Marlow Vance Photography">
      <text class="brand-name" x="801" y="455" text-anchor="middle">MARLOW VANCE</text>
      <text class="brand-tagline" x="801" y="540" text-anchor="middle">........Photography........</text>
    </svg>
  </main>
</body>
</html>
```